Business Card and Letterhead for Juniper Anvil - (Have Logo)

Update 4: Removed company reg no from business card details as it looked a bit out of place. Updated services list.
UPDATE 3
Sorry, I got the address a little bit wrong, have updated it below. Sorry for any inconvenience caused.
UPDATE 2
Finally I have the details for the business cards and letterhead. Submissions already made do not have to be updated unless shortlisted, if all new submissions could include the details for me, Marcus, that would be very much appreciated and help with the final shortlist selection. I intend to share a shortlist of the three best entries with past and existing customers for their feedback and opinions. Thank you all again for your time.
Here are the details.
Marcus Telby
Web Developer
T: 01632 960 418
E: marcus@juniperanvil.example
www.juniperanvil.example
Professional Photography
Web Solutions & E-Commerce
Audio & HD Video Production
Marketing & Promotions
Identity and Branding
Juniper Anvil Ltd
Suite 20938, 3rd Floor
212-224 Orchard Lane
London, N7 9QX
Company Reg. No: 05829147
The order and the layout of the information are of course down to the design, but the company registration number should be smaller and less prominent. The formatting of the telephone and email address using a T: and an E: I am not sure about and again if it is Tel: or Email: or Icons is up to the design.
The Company No. on the letterhead should read (somewhere in small text along the bottom):
Juniper Anvil is a Ltd Company registered in England & Wales, Registration No. 05829147.
The second business card details are
Oliver Brackley
Photographer
T: 01632 960 418
E: oliver@juniperanvil.example
Everything else the same of course.
Thank you again for all the submissions so far.
END OF UPDATE 2
-
UPDATE 1: Please do not alter the logo nor the logo colours. (This was a previous pixel forum project and I am extremely happy with it. The icon can stand alone of course, but I have had to eliminate all entries that have made it black and white, or reversed the icon.) I would like to thank everyone that has participated so far and am very grateful for all your thought and time.
End of Update 1
-
Original Brief:
I have attached the logo vector file.
Following a superb logo from a previous Pixel Forum project I am now looking for a business card design and (although less important) a letterhead as well.
I must admit I tried to do it myself but could only come up with the usual amateur stuff that in comparison to the quality of the logo looked awful.
About Us
Juniper Anvil Ltd will be a new company due to start in January. It is really just me (a web developer) and my friend (a photographer). We will be aiming at the usual small to medium sized businesses in the local area, selling various digital services including photographic services to the public, web hosting and development, commercial photography, modelling services (not us!), full video and film production and possibly a bit of marketing as well. (Really it is anything we can do professionally all lumped together! We met running seperate businesses which have both since closed)
We will not be competing on price. We plan to be expensive but fair. Certainly not the cheapest.
What we are looking for
Business Card
I imagine a double sided business card, which will be used for more than one person. I imagine the front to be the same for everyone and the persons details to be on the back, although this is of course only my thoughts and I am of course completely open to any ideas.
The card could also have a services list or a bit about what we do on it. It might feature the website address, our business address (mail forwarding address) or our registered company number.
Or it might have none of that, we are completely open to any ideas and have no real fixed opinions. I just want it to be really nice :-)
Letterhead (secondary importance)
We will make our decision primarily on the business card, although a mathcing letterhead would be fantastic. Something standardish in format and simple, although again, all ideas are welcomed.
I hope that is enough information but if you have any questions I will answer them as fully and as quickly as possible.
Thank you once again and I really look forward to seeing your ideas and picking a winner.
Marcus T.
Small businesses AND the general public
Film Production

```html
<!DOCTYPE html>
<html lang="en">
<head>
<meta charset="utf-8">
<title>Juniper Anvil – Business Card and Letterhead</title>
<link rel="stylesheet" href="https://fonts.googleapis.com/css2?family=Source+Sans+3:wght@400;600;700&display=swap">
<style>
  :root {
    --red: #b3151e;
    --red-deep: #8f1017;
    --ink: #3a3a3c;
    --charcoal: #333335;
    --paper: #ffffff;
    --grey-soft: #f4f3f4;
    --grey-mid: #9a9a9a;
    --stage-dark: #0b0d0d;
    --stage-light: #5b6764;
  }
  * { margin: 0; padding: 0; box-sizing: border-box; }
  html, body { width: 1200px; height: 900px; overflow: hidden; }
  body {
    position: relative;
    font-family: "Source Sans 3", "Myriad Pro", sans-serif;
    background: radial-gradient(ellipse 70% 80% at 38% 100%, var(--stage-light) 0%, #2a3230 45%, var(--stage-dark) 80%);
  }
  .abs { position: absolute; }

  /* wordmark */
  .wordmark { display: flex; align-items: center; gap: 5px; }
  .wordmark .mark-square { background: var(--red); }
  .wordmark .mark-name {
    color: var(--ink); font-weight: 700; letter-spacing: .5px; white-space: nowrap; line-height: 1;
  }

  .pixel-field { position: absolute; }

  /* front card */
  .card-front {
    left: 103px; top: 87px; width: 268px; height: 159px;
    background: var(--paper); border-radius: 10px; overflow: hidden;
  }
  .card-front .tab { left: 182px; top: 0; width: 86px; height: 19px; background: var(--charcoal); }
  .card-front .wordmark { left: 8px; top: 10px; }
  .card-front .mark-square { width: 14px; height: 14px; }
  .card-front .mark-name { font-size: 16px; }
  .card-front .company { left: 23px; top: 47px; color: var(--red); font-weight: 700; font-size: 11.5px; }
  .card-front .address { left: 23px; top: 61px; font-size: 7px; line-height: 9px; color: #111; font-weight: 600; }
  .card-front .person { left: 180px; top: 43px; width: 80px; text-align: center; }
  .card-front .person-name { font-weight: 700; font-size: 11px; color: #111; }
  .card-front .person-role { font-size: 7px; color: #222; margin-top: 1px; }
  .card-front .contact-band { left: 0; top: 89px; width: 175px; height: 70px; background: var(--red); }
  .card-front .contact { left: 23px; top: 100px; color: #fff; font-size: 8.6px; line-height: 11.5px; }
  .card-front .contact dt { float: left; width: 31px; clear: left; }
  .card-front .contact dd { margin-left: 31px; }
  .card-front .pixel-field { left: 175px; top: 89px; width: 56px; height: 70px;
    background: linear-gradient(135deg, #8a8a8a 0%, #e6e6e6 40%, #f3dede 70%, #c85058 100%); }
  .card-front .corner-red { left: 231px; top: 89px; width: 37px; height: 42px; background: var(--red); }
  .card-front .corner-dark { left: 231px; top: 131px; width: 37px; height: 14px; background: var(--charcoal); }

  /* back card */
  .card-back {
    left: 110px; top: 295px; width: 268px; height: 159px;
    background: var(--paper); border-radius: 10px; overflow: hidden;
  }
  .card-back .wordmark { left: 55px; top: 16px; }
  .card-back .mark-square { width: 18px; height: 18px; }
  .card-back .mark-name { font-size: 20px; }
  .card-back .service-band { left: 0; top: 58px; width: 268px; height: 101px;
    background: linear-gradient(90deg, var(--red) 0%, var(--red) 55%, var(--red-deep) 100%); }
  .card-back .pixel-field { left: 140px; top: 58px; width: 128px; height: 101px;
    background: linear-gradient(160deg, #c0323a 0%, #9e1219 50%, #d04048 100%); }
  .card-back .url-bar { left: 0; top: 58px; width: 90px; height: 14px; background: var(--charcoal);
    color: #fff; font-size: 6px; line-height: 14px; padding-left: 5px; font-weight: 600; }
  .card-back .url-steps { left: 90px; top: 58px; width: 47px; height: 14px;
    background: linear-gradient(90deg, #6e6e6e 0 33%, #a6a6a6 33% 66%, #d8d8d8 66%); }
  .card-back .ghost-square { left: 4px; top: 80px; width: 50px; height: 75px; background: rgba(255,255,255,.08); }
  .card-back .services { left: 81px; top: 85px; color: #fff; }
  .card-back .services h3 { font-size: 9px; font-weight: 700; margin-bottom: 4px; }
  .card-back .services li { list-style: none; font-size: 7.5px; line-height: 10px; font-weight: 600; }
  .card-back .services li::before { content: "▪ "; font-size: 6px; }

  /* letterhead */
  .letterhead { left: 437px; top: 0; width: 690px; height: 900px; background: var(--paper); }
  .letterhead .top-rule { left: 0; top: 5px; width: 183px; height: 7px; background: var(--charcoal); }
  .letterhead .top-steps { left: 183px; top: 5px; width: 26px; height: 7px;
    background: linear-gradient(90deg, #888 0 33%, #bbb 33% 66%, #ddd 66%); }
  .letterhead .pixel-field { left: 262px; top: 5px; width: 53px; height: 68px;
    background: linear-gradient(120deg, #cfcfcf 0%, #ffffff 45%, #d88a8f 100%); }
  .letterhead .head-band { left: 305px; top: 5px; width: 355px; height: 68px; background: var(--red); }
  .letterhead .head-cap { left: 660px; top: 5px; width: 30px; height: 68px; background: var(--charcoal); }
  .letterhead .wordmark { left: 23px; top: 36px; }
  .letterhead .mark-square { width: 24px; height: 24px; }
  .letterhead .mark-name { font-size: 27px; }
  .letterhead .contact { left: 512px; top: 12px; color: #fff; font-size: 10.5px; line-height: 13px; }
  .letterhead .contact dt { float: left; width: 15px; clear: left; }
  .letterhead .contact dd { margin-left: 15px; }
  .letterhead .company { left: 23px; top: 93px; color: var(--red); font-weight: 700; font-size: 13.5px; }
  .letterhead .address { left: 23px; top: 108px; font-size: 9.5px; line-height: 13px; color: #111; font-weight: 600; }
  .letterhead .ghost-square { left: 11px; top: 757px; width: 267px; height: 103px; background: var(--grey-soft); }
  .letterhead .foot-line { left: 0; top: 864px; width: 690px; height: 3px; background: var(--red); }
  .letterhead .foot-band { left: 0; top: 870px; width: 690px; height: 28px; background: var(--charcoal); }
  .letterhead .foot-url { right: 17px; top: 878px; color: #fff; font-size: 10px; }
</style>
</head>
<body>

  <section class="abs card-front" aria-label="Business card, front">
    <div class="abs tab"></div>
    <div class="abs wordmark"><span class="mark-square"></span><span class="mark-name">JUNIPER ANVIL</span></div>
    <p class="abs company">JUNIPER ANVIL</p>
    <p class="abs address">417 Alder Row Fenwick Park,JL 3190<br>Marlow Bay, Quebec H9Q2K4</p>
    <div class="abs person">
      <p class="person-name">Dara Wellson</p>
      <p class="person-role">Manger</p>
    </div>
    <div class="abs contact-band"></div>
    <dl class="abs contact">
      <dt>Phone</dt><dd>: 555-014-2231</dd>
      <dt>Fax</dt><dd>: 555-014-7780</dd>
      <dt>Email</dt><dd>: info@juniperanvil.example</dd>
      <dt>Web</dt><dd>: www.juniperanvil.example</dd>
    </dl>
    <div class="pixel-field" role="img" aria-label="Scattered grey and red pixel pattern"></div>
    <div class="abs corner-red"></div>
    <div class="abs corner-dark"></div>
  </section>

  <section class="abs card-back" aria-label="Business card, back">
    <div class="abs wordmark"><span class="mark-square"></span><span class="mark-name">JUNIPER ANVIL</span></div>
    <div class="abs service-band"></div>
    <div class="pixel-field" role="img" aria-label="Red pixel mosaic pattern"></div>
    <div class="abs ghost-square"></div>
    <p class="abs url-bar">www.juniperanvil.example</p>
    <div class="abs url-steps"></div>
    <div class="abs services">
      <h3>OUR SERVICES</h3>
      <ul>
        <li>Photographic services</li>
        <li>Web hosting &amp; development</li>
        <li>Modelling services</li>
        <li>Full video and film production</li>
      </ul>
    </div>
  </section>

  <section class="abs letterhead" aria-label="Letterhead">
    <div class="abs top-rule"></div>
    <div class="abs top-steps"></div>
    <div class="abs head-band"></div>
    <div class="pixel-field" role="img" aria-label="Scattered grey and red pixel pattern"></div>
    <div class="abs head-cap"></div>
    <div class="abs wordmark"><span class="mark-square"></span><span class="mark-name">JUNIPER ANVIL</span></div>
    <dl class="abs contact">
      <dt>P</dt><dd>: 555-014-2231</dd>
      <dt>F</dt><dd>: 555-014-7780</dd>
      <dt>E</dt><dd>: info@juniperanvil.example</dd>
      <dt>W</dt><dd>: www.juniperanvil.example</dd>
    </dl>
    <p class="abs company">JUNIPER ANVIL</p>
    <p class="abs address">417 Alder Row Fenwick Park,JL 3190<br>Marlow Bay, Quebec H9Q2K4</p>
    <div class="abs ghost-square"></div>
    <div class="abs foot-line"></div>
    <div class="abs foot-band"></div>
    <p class="abs foot-url">www.juniperanvil.example</p>
  </section>

</body>
</html>
```